Banner for a National Dental Conference

We need a banner logo for our next Dental Conference in 2017. Our theme is 'Challenging the Status Quo'.
It must have the words '20 years of oral health therapy in Victoria' and the conference date and venue:
7-8th April 2017
Wattlebrook Shore Lodge, Torquay, Victoria.
It must also feature our association logo as attached.
Please be creative, however, we would like a 'clean' design, not cluttered.
The design is intended for use in the conference program and website.

Target Market(s)

Dental practitioners

Industry/Entity Type

Dental

Requirements
Must have
• As above.

```html
<!DOCTYPE html>
<html lang="en">
<head>
<meta charset="utf-8">
<title>Oral Health Therapy Conference Banner</title>
<link rel="stylesheet" href="https://fonts.googleapis.com/css2?family=Josefin+Sans:wght@300;400;600&family=Michroma&display=swap">
<style>
  :root {
    --backdrop-deep: #7e0b2c;
    --backdrop-mid: #a4153d;
    --backdrop-light: #b92049;
    --card-white: #ffffff;
    --guild-purple: #5a2d88;
    --headline-green: #3f7d60;
    --headline-gold: #f3b94d;
    --band-orange: #f5ad45;
    --band-orange-light: #f8c060;
    --list-blue: #2b80b2;
    --list-divider: rgba(255,255,255,0.22);
    --footer-tint: #edf3f6;
    --footer-text: #1f9ad6;
    --light-text: #ffffff;
  }
  * { box-sizing: border-box; margin: 0; padding: 0; }
  html, body { width: 758px; height: 1200px; overflow: hidden; }
  body {
    background: radial-gradient(ellipse at 50% 45%, var(--backdrop-light) 0%, var(--backdrop-mid) 55%, var(--backdrop-deep) 100%);
    position: relative;
    font-family: 'Josefin Sans', sans-serif;
  }
  .banner {
    position: absolute;
    left: 132px;
    top: 118px;
    width: 493px;
    height: 984px;
    box-shadow: 0 2px 10px rgba(0,0,0,0.35);
    overflow: hidden;
  }
  .banner__hero {
    position: relative;
    height: 493px;
    background: var(--card-white);
    border: 2px solid #e6e6e6;
    border-bottom: none;
    text-align: center;
  }
  .banner__emblem {
    position: absolute;
    left: 46px;
    top: 110px;
    width: 400px;
    height: 383px;
    border-radius: 200px 200px 0 0;
    background: radial-gradient(ellipse at 50% 40%, rgba(200,200,200,0.26) 0%, rgba(220,220,220,0.12) 55%, rgba(255,255,255,0) 75%);
  }
  .guild-name {
    position: relative;
    padding-top: 52px;
    font-weight: 600;
    font-size: 34px;
    line-height: 42px;
    letter-spacing: 0.5px;
    color: var(--guild-purple);
  }
  .headline {
    position: relative;
    margin-top: 70px;
    font-weight: 300;
    font-size: 46px;
    line-height: 68px;
    letter-spacing: 0.5px;
    color: var(--headline-green);
  }
  .headline__accent { color: var(--headline-gold); }
  .headline__place {
    display: block;
    font-size: 24px;
    line-height: 40px;
    letter-spacing: 4px;
    color: var(--headline-green);
  }
  .banner__band {
    height: 69px;
    display: flex;
    align-items: center;
    justify-content: space-between;
    padding: 0 30px 0 36px;
    background: linear-gradient(180deg, var(--band-orange-light), var(--band-orange));
    color: var(--light-text);
    font-family: 'Michroma', sans-serif;
    font-size: 15px;
    letter-spacing: 1.5px;
    white-space: nowrap;
  }
  .banner__list {
    height: 351px;
    background: var(--list-blue);
    list-style: none;
  }
  .venue-row {
    height: 87.75px;
    display: flex;
    align-items: center;
    justify-content: space-between;
    padding: 0 30px 0 40px;
    border-bottom: 1px solid var(--list-divider);
    color: var(--light-text);
    font-family: 'Michroma', sans-serif;
    font-size: 15px;
    letter-spacing: 1.5px;
    white-space: nowrap;
  }
  .venue-row:last-child { border-bottom: none; }
  .banner__footer {
    height: 71px;
    display: flex;
    align-items: center;
    justify-content: center;
    background: linear-gradient(180deg, #f6f9fb, var(--footer-tint));
    color: var(--footer-text);
    font-family: 'Michroma', sans-serif;
    font-size: 27px;
    letter-spacing: 5px;
  }
</style>
</head>
<body>
  <main class="banner">
    <section class="banner__hero">
      <div class="banner__emblem" role="img" aria-label="Faint caduceus emblem behind the headline"></div>
      <div class="guild-name">Southbay Dental Guild</div>
      <h1 class="headline">
        20 YEARS OF<br>ORAL HEALTH<br><span class="headline__accent">THERAPY</span>
        <span class="headline__place">IN VICTORIA</span>
      </h1>
    </section>
    <div class="banner__band">
      <span>Challenging the Status Quo</span>
      <svg width="22" height="22" viewBox="0 0 22 22" aria-hidden="true"><path d="M2 4 L11 19 L20 4 L11 9 Z" fill="#ffffff"/></svg>
    </div>
    <ul class="banner__list">
      <li class="venue-row"><span>7–8 APRIL 2017</span><svg width="26" height="22" viewBox="0 0 26 22" aria-hidden="true"><path d="M1 1 L25 11 L1 21 L7 11 Z" fill="#ffffff"/></svg></li>
      <li class="venue-row"><span>WATTLEBROOK SHORE LODGE</span><svg width="26" height="22" viewBox="0 0 26 22" aria-hidden="true"><path d="M1 1 L25 11 L1 21 L7 11 Z" fill="#ffffff"/></svg></li>
      <li class="venue-row"><span>TORQUAY</span><svg width="26" height="22" viewBox="0 0 26 22" aria-hidden="true"><path d="M1 1 L25 11 L1 21 L7 11 Z" fill="#ffffff"/></svg></li>
      <li class="venue-row"><span>VICTORIA</span><svg width="26" height="22" viewBox="0 0 26 22" aria-hidden="true"><path d="M1 1 L25 11 L1 21 L7 11 Z" fill="#ffffff"/></svg></li>
    </ul>
    <div class="banner__footer">LEARN MORE &gt;&gt;</div>
  </main>
</body>
</html>
```